Health & Nutrition - Business Cards

Needs to look new-age, simple, and elegant. The cards are for my services/counsel in health and nutrition - which include mind, body, and soul. I would like to see something clean and simple but beautiful. Can have a plain background or with a pattern but I don't want it to take away from my contact details. Therefore, my info can be on the back of the card and a nice front design. I really like the flower of life symbol. The name of my business is called Willow Lantern.

Target Market(s)

Clients - men & women age 20-60. Adults, parents, teachers, sick individuals seeking nutrient counseling and dietary management.

Industry/Entity Type

Nutritionist

Contact Information for Business Card

Tomas Brindle
Cell: 345-582-7046
Email: tbrindle@mailvane.net

Colors
33a6d7
33b8a4
add136
ffffff
5c5c5c
f04a50
fbee3f
cedeed
85cae6

Requirements
Nice to have
• Maybe it can have some sort of sacred geometry as well, but not required. Nice to have the colors that I choose in the project but feel free to come up with your own use of colors. Thanks! =)

```html
<!DOCTYPE html>
<html lang="en">
<head>
<meta charset="utf-8">
<title>Willow Lantern – Business Cards</title>
<link rel="stylesheet" href="https://fonts.googleapis.com/css2?family=PT+Serif:wght@400;700&display=swap">
<style>
  :root {
    --backdrop: #67fea6;
    --ink: #3c4a52;
    --paper: #ffffff;
    --rose: #fe2461;
    --sun: #f6fd30;
    --lime: #a2fd1a;
    --mint: #4afd89;
    --slate: #3c4a52;
  }
  * { margin: 0; padding: 0; box-sizing: border-box; }
  html, body { width: 1200px; height: 1200px; overflow: hidden; }
  body {
    background: var(--backdrop);
    font-family: "PT Serif", Georgia, serif;
    position: relative;
  }
  .card {
    position: absolute;
    left: 298px;
    width: 604px;
    height: 344px;
    overflow: hidden;
    box-shadow: 0 14px 36px rgba(20, 90, 50, 0.28);
  }
  .card--front { top: 198px; }
  .card--back { top: 658px; background: var(--paper); }

  .front-art { position: absolute; inset: 0; width: 100%; height: 100%; display: block; }
  .front-art .tri-rose { fill: var(--rose); }
  .front-art .tri-sun { fill: var(--sun); }
  .front-art .field-lime { fill: var(--lime); }
  .front-art .field-mint { fill: var(--mint); }
  .front-art .diamond { fill: var(--slate); }

  .front-mark {
    position: absolute;
    left: 0; right: 0;
    top: 146px;
    text-align: center;
    color: var(--paper);
    font-size: 23px;
    line-height: 1.15;
  }
  .front-name {
    position: absolute;
    left: 0; right: 0;
    top: 297px;
    text-align: center;
    color: var(--paper);
    font-size: 38px;
    line-height: 1;
  }

  .back-panel {
    position: absolute;
    right: 0; top: 0;
    width: 218px; height: 100%;
    background: var(--slate);
    display: flex;
    align-items: center;
    justify-content: center;
  }
  .back-mark {
    color: var(--paper);
    font-size: 24px;
    line-height: 1.15;
    text-align: center;
  }
  .line {
    position: absolute;
    left: 22px;
    color: var(--ink);
    line-height: 1;
    white-space: nowrap;
  }
  .business { top: 16px; font-size: 38px; }
  .tagline { top: 55px; font-size: 18px; }
  .person { top: 215px; font-size: 38px; }
  .role { top: 254px; font-size: 18px; }
  .cell { top: 288px; font-size: 18px; }
  .email { top: 311px; font-size: 18px; }
</style>
</head>
<body>
  <section class="card card--front">
    <svg class="front-art" viewBox="0 0 755 431" preserveAspectRatio="none" aria-hidden="true">
      <rect class="field-mint" x="0" y="0" width="755" height="431"/>
      <polygon class="field-lime" points="0,0 218,216 431,431 0,431"/>
      <polygon class="tri-rose" points="0,0 431,0 378,56 218,216"/>
      <polygon class="tri-sun" points="431,0 755,0 538,216 378,56"/>
      <polygon class="diamond" points="378,56 538,216 378,376 218,216"/>
    </svg>
    <div class="front-mark">Willow<br>Lantern</div>
    <div class="front-name">Willow Lantern</div>
  </section>

  <section class="card card--back">
    <div class="line business">Willow Lantern</div>
    <div class="line tagline">Health &amp; Nutritions</div>
    <div class="line person">Tomas Brindle</div>
    <div class="line role">Nutritionist</div>
    <div class="line cell">Cell: 345-582-7046</div>
    <div class="line email">Email: tbrindle@mailvane.net</div>
    <div class="back-panel">
      <div class="back-mark">Willow<br>Lantern</div>
    </div>
  </section>
</body>
</html>
```